Granite Ridge Holdings

I have a real estate investment business.

** I need editable vector files of the final design.

Industry/Entity Type

Real Estate

Contact Information for Business Card

I would like the card to be clear and direct with the company name and contact info. I would prefer not to have a design that is too busy (i.e., with excessive detail) in the business card.

Font styles to use
Sans Serif

Requirements
Must have
• My card must have the following information listed below:
• Company name: Grainite Ridge Holdings LLC
• My name: Daniel Vorsley
• Phone number: (555) 218-9067
• Email address: dtvorsley@mailbox-example.net
• Keywords: “Real Estate Investments”
Nice to have
• I would like to have a design that resembles the characteristics/uses of obsidian stone which resembles something related to strength and resilience. Perhaps something with sharp, sleek color transitions as well.

```html
<!DOCTYPE html>
<html lang="en">
<head>
<meta charset="utf-8">
<title>Grainite Ridge Holdings LLC – Business Card</title>
<link rel="stylesheet" href="https://fonts.googleapis.com/css2?family=Josefin+Sans:wght@600&family=PT+Serif&display=swap">
<style>
  :root {
    --canvas: #b3b3b3;
    --card-light: #ffffff;
    --card-stone: #d9d9d9;
    --band: #8c8c8c;
    --ink: #0a0a0a;
    --paper: #f7f7f7;
  }
  * { box-sizing: border-box; margin: 0; padding: 0; }
  html, body { width: 1130px; height: 1200px; overflow: hidden; background: #fff; }
  .canvas {
    position: relative; width: 1130px; height: 1200px;
    background: var(--canvas); border-radius: 12px; overflow: hidden;
  }
  .card { position: absolute; width: 579px; height: 358px; overflow: hidden; }
  .card--front { left: 251px; top: 205px; }
  .card--back { left: 252px; top: 617px; }
  .stone-texture {
    position: absolute; inset: 0;
    background:
      linear-gradient(90deg, rgba(200,200,200,.55) 0%, rgba(255,255,255,0) 30%),
      radial-gradient(circle at 60% 45%, var(--card-light) 0%, var(--card-stone) 100%);
  }
  .brand {
    font-family: "Josefin Sans", sans-serif; font-weight: 600;
    color: var(--ink); text-transform: uppercase; white-space: nowrap; line-height: 1;
  }
  .card--front .brand {
    position: absolute; right: 21px; top: 40px; font-size: 26px;
    background: var(--card-light); padding: 4px 8px 1px; border-radius: 14px;
  }
  .name-tab {
    position: absolute; left: 0; top: 138px; width: 330px; height: 81px;
    background: var(--band); border-radius: 0 41px 41px 0;
  }
  .name {
    position: absolute; right: 58px; top: 20px;
    font-family: "Josefin Sans", sans-serif; font-weight: 600; line-height: 1.1;
    font-size: 28px; color: var(--ink); text-transform: uppercase; white-space: nowrap;
  }
  .role {
    position: absolute; right: 58px; top: 53px;
    font-family: "Josefin Sans", sans-serif; font-weight: 600;
    font-size: 10.5px; color: var(--paper); text-transform: uppercase; white-space: nowrap;
  }
  .rule { position: absolute; left: 330px; top: 178px; width: 236px; height: 2.5px; background: var(--ink); }
  .contact-band {
    position: absolute; left: 0; top: 252px; width: 100%; height: 63px;
    background: var(--band);
    font-family: "PT Serif", serif; color: var(--paper);
  }
  .contact {
    position: absolute; top: 0; height: 63px;
    display: flex; align-items: center; gap: 10px; white-space: nowrap;
  }
  .contact--phone { left: 36px; font-size: 17px; }
  .contact--email { right: 22px; font-size: 15.5px; }
  .contact svg { flex: none; }
  .back-title {
    position: absolute; left: 28px; top: 159px; width: 522px; height: 41px;
    background: var(--card-light); border-radius: 21px;
    display: flex; align-items: center; justify-content: center;
  }
  .back-title .brand { font-size: 29px; padding-top: 5px; }
  .keyword-bar {
    position: absolute; left: 28px; top: 326px; width: 518px; height: 23px;
    background: var(--band); border-radius: 12px;
    font-family: "PT Serif", serif; font-size: 16px; color: var(--paper);
    display: flex; align-items: center; justify-content: center; white-space: nowrap;
  }
</style>
</head>
<body>
<main class="canvas">
  <section class="card card--front" aria-label="Business card front">
    <div class="stone-texture" role="img" aria-label="Light grey stone-cell mosaic texture"></div>
    <h1 class="brand">Grainite Ridge Holdings LLC</h1>
    <div class="name-tab">
      <p class="name">Daniel Vorsley</p>
      <p class="role">Grand Manager</p>
    </div>
    <div class="rule"></div>
    <div class="contact-band">
      <p class="contact contact--phone">
        <svg width="16" height="16" viewBox="0 0 24 24" aria-hidden="true"><path fill="#0a0a0a" d="M6.6 10.8a15.1 15.1 0 0 0 6.6 6.6l2.2-2.2c.3-.3.7-.4 1-.2 1.1.4 2.3.6 3.6.6.6 0 1 .4 1 1V20c0 .6-.4 1-1 1A17 17 0 0 1 3 4c0-.6.4-1 1-1h3.5c.6 0 1 .4 1 1 0 1.3.2 2.5.6 3.6.1.3 0 .7-.2 1z"/></svg>
        (555) 218-9067
      </p>
      <p class="contact contact--email">
        <svg width="20" height="15" viewBox="0 0 20 15" aria-hidden="true"><rect x="1" y="1" width="18" height="13" fill="none" stroke="#0a0a0a" stroke-width="1.5"/><path d="M1 1l9 7 9-7M1 14l7-6M19 14l-7-6" fill="none" stroke="#0a0a0a" stroke-width="1.3"/></svg>
        dtvorsley@mailbox-example.net
      </p>
    </div>
  </section>

  <section class="card card--back" aria-label="Business card back">
    <div class="stone-texture" role="img" aria-label="Grey stone-cell mosaic texture"></div>
    <div class="back-title"><h2 class="brand">Grainite Ridge Holdings LLC</h2></div>
    <p class="keyword-bar">Real Estate Investments</p>
  </section>
</main>
</body>
</html>
```